Lease-A-Goose's web page

I need a web page(s) to show and promote my business of renting chickens. We provide seasonal rentals in the United States of a layer hen package for people who would like to try raising their own chickens. The package includes two hens, coop, attached run, feeder, waterer, and food. I would like interested people to be able to fill out a form so that I can have partners contact them to set up a delivery in their area. Our service is very popular with urban and suburban families.

Target Market(s)

Urban foodies.
Families.
People interested in Organic Foods.
People concerned with where their food comes from and how it is grown/prepared.
People interested in Urban Farming.

Industry/Entity Type

Business

Requirements
Must have
• A way for me to see rental interest based on zip code.
• A contact form including zip code, e-mail, and optional phone number.
• Our Logo. (Please contact if you are unable to use the file I provided.)
Nice to have
• A guest book for former renters that we can vet before posting.

```html
<!DOCTYPE html>
<html lang="en">
<head>
<meta charset="utf-8">
<title>Lease-A-Goose</title>
<link href="https://fonts.googleapis.com/css2?family=Ubuntu:ital,wght@0,400;0,500;0,700;1,500;1,700&family=Dancing+Script:wght@700&display=swap" rel="stylesheet">
<style>
:root{
  --wood:#5a3a22;
  --wood-dark:#3e2717;
  --cream:#efe7d8;
  --paper:#f4eee2;
  --brown:#3a2f27;
  --rust:#8c3a1c;
  --orange:#e2650f;
  --maroon:#6b0d0d;
  --red:#c4281f;
  --text:#4a3b33;
  --footer:#2a2826;
  --muted:#a9a39a;
}
*{box-sizing:border-box;margin:0;padding:0}
html,body{width:1045px;height:1200px;overflow:hidden}
body{position:relative;font-family:"Ubuntu",sans-serif;background:var(--paper);color:var(--text)}
.abs{position:absolute}
.hero{left:0;top:0;width:1045px;height:412px;background:linear-gradient(180deg,#9a8f80 0%,#6f6a4e 35%,#5d7a3a 70%,#c9875a 100%)}
.topbar{left:0;top:0;width:1045px;height:46px;background:linear-gradient(180deg,#6b4529,var(--wood-dark));box-shadow:0 2px 4px rgba(0,0,0,.4)}
.nav{right:74px;top:15px;display:flex;gap:29px;list-style:none}
.nav li{color:#f2e6d8;font-size:10px;font-weight:500;letter-spacing:.2px}
.nav li.active{color:#fff;border-bottom:2px solid var(--red);padding-bottom:3px}
.logo{left:15px;top:0;width:212px;height:149px;background:#fff;box-shadow:0 2px 6px rgba(0,0,0,.4);display:flex;align-items:center;justify-content:center;gap:7px;clip-path:polygon(0 0,100% 0,100% 88%,50% 100%,0 88%)}
.logo .dot{width:14px;height:14px;border-radius:50%;background:var(--red)}
.logo span{font-weight:700;font-size:19px;color:var(--red)}
.caption{left:223px;top:215px;width:573px;height:101px;background:rgba(40,40,40,.72);text-align:center;color:#eee}
.caption h1{font-weight:500;font-size:28px;margin-top:11px;color:#e8e8e8}
.caption p{font-family:"Dancing Script",cursive;font-size:24px;margin-top:6px}
.arrow{width:40px;height:40px;border-radius:50%;background:rgba(200,60,30,.85);top:231px}
.arrow svg{display:block}
.ph{border:1px solid #fff;box-shadow:0 0 0 1px #ccc}
.feat h3{font-style:italic;font-weight:700;color:var(--orange);font-size:12px}
.feat p{font-style:italic;font-weight:500;color:#6b5d52;font-size:9.5px;line-height:12px}
.about h2{font-family:"Dancing Script",cursive;color:var(--rust);font-size:32px;font-weight:700}
.about h4{font-weight:700;font-size:13px;color:#3a332d}
.body{font-size:10px;line-height:17px;color:#3f3a35}
.rent{color:var(--maroon);font-size:10.5px}
.price{color:var(--orange);font-style:italic;font-weight:700;font-size:14px;word-spacing:4px}
.panel{left:128px;top:870px;width:792px;height:156px;background:var(--brown);border-radius:6px}
.panel .sep{top:0;width:1px;height:156px;background:#4e443b}
.panel h5{color:#fff;font-weight:500;font-size:14px;letter-spacing:.5px}
.btn{background:var(--maroon);color:#fff;font-weight:700;font-size:9.5px;text-align:center;border-radius:2px}
.field{width:190px;height:16px;background:#fff;font-size:8px;color:#555;padding:3px 6px}
.footer{left:0;top:1040px;width:1045px;height:160px;background:var(--footer)}
.footer h6{color:var(--muted);font-size:10.5px;font-weight:700;letter-spacing:.4px}
.fb{left:434px;top:1051px;width:241px;height:110px;background:#fff;border:1px solid #ccc;font-size:8px;color:#333}
.fb .av{width:41px;height:33px;background:linear-gradient(#b9b2a8,#7d746a)}
.sq{width:25px;height:21px;border-radius:3px}
.flinks{left:108px;top:1176px;display:flex;gap:14px;font-size:8.5px;color:#ddd}
</style>
</head>
<body>

<div class="abs hero" role="img" aria-label="Hens and a rooster on a lawn before a coop, with a basket of eggs in front"></div>
<div class="abs topbar"></div>
<ul class="abs nav">
  <li class="active">HOME</li><li>ABOUT US</li><li>PRODUCTS</li><li>SERVICES</li><li>FAQ'S</li><li>CONTACT US</li><li>PARTNER REGISTER</li>
</ul>
<div class="abs logo"><div class="dot"></div><span>Lease-A-Goose</span></div>

<div class="abs caption">
  <h1>Chickens at Home</h1>
  <p>Chickens, Coops and Accessories Delivered To Your Door</p>
</div>
<div class="abs arrow" style="left:28px"><svg width="40" height="40"><path d="M23 12 L15 20 L23 28" stroke="#fff" stroke-width="3.5" fill="none"/></svg></div>
<div class="abs arrow" style="left:979px"><svg width="40" height="40"><path d="M17 12 L25 20 L17 28" stroke="#fff" stroke-width="3.5" fill="none"/></svg></div>

<section class="feat">
  <div class="abs ph" style="left:125px;top:437px;width:256px;height:113px;background:linear-gradient(135deg,#b98a4c,#7d6a52)" role="img" aria-label="Golden hens pecking in straw"></div>
  <div class="abs ph" style="left:393px;top:437px;width:256px;height:113px;background:linear-gradient(135deg,#4c3a22,#a58a52)" role="img" aria-label="Group of dark chicks under a heat lamp"></div>
  <div class="abs ph" style="left:664px;top:437px;width:256px;height:113px;background:radial-gradient(circle at 55% 55%,#d9b8a2,#1a1410 70%)" role="img" aria-label="Hand holding a small egg next to a coin"></div>
  <div class="abs" style="left:127px;top:556px;width:250px"><h3>Our Products</h3><p>the package includes two hens, coop, attached run, feeder, waterer, and food</p></div>
  <div class="abs" style="left:406px;top:556px;width:240px"><h3>Services</h3><p>products delivered to your door-step</p></div>
  <div class="abs" style="left:679px;top:556px;width:240px"><h3>Pricing &amp; Accessories</h3><p>chickens, coops and accessories</p></div>
</section>

<section class="about">
  <div class="abs" style="left:0;top:616px;width:385px;height:238px;background:linear-gradient(90deg,#9c5a2a 0%,#b8773f 45%,#d8cdb8 100%)" role="img" aria-label="Brown hens standing in grass"></div>
  <h2 class="abs" style="left:366px;top:608px">Chicken Rental, Purchasing, Coops and Feeds</h2>
  <h4 class="abs" style="left:393px;top:655px">Be a fair weather farmer.</h4>
  <p class="abs body" style="left:393px;top:675px;width:540px">We rent chickens (including 2 hens, coop, run, accessories, and food) for people to have farm fresh eggs and the joys of chicken ownership in their own back yards. We deliver and set up in the spring and pick up in the fall. Take your winters off and become a fair weather farmer.</p>
  <p class="abs body" style="left:393px;top:729px;width:540px">Come on down to the Maple Harvest Fair and visit some of our hens at the Greenfield Expo. Tilly's Reclaim has a coop constructed entirely out of salvaged materials. Great ideas!</p>
  <p class="abs rent" style="left:461px;top:775px">Rental Charges &nbsp;: &nbsp;Try our chooks for as long as you like!</p>
  <p class="abs price" style="left:494px;top:797px">1 week &nbsp;$40* &nbsp; 1 month &nbsp;$180*</p>
  <p class="abs rent" style="left:400px;top:823px">or rent for a shorter or longer period! Delivery fee and bond apply to all rentals.</p>
</section>

<section class="abs panel">
  <div class="abs sep" style="left:263px"></div>
  <div class="abs sep" style="left:528px"></div>
  <h5 class="abs" style="left:43px;top:21px">AVAILABLE CHICKENS!</h5>
  <p class="abs" style="left:22px;top:56px;font-style:italic;font-weight:700;font-size:9px;color:#b9b0a5">Ask about our Breed</p>
  <div class="abs btn" style="left:29px;top:76px;width:90px;height:22px;line-height:22px;font-style:italic">VIEW HENS</div>
  <div class="abs" style="left:149px;top:49px;width:93px;height:57px;border:3px solid #fff;background:linear-gradient(180deg,#9cc4e0,#e8e4dc)" role="img" aria-label="White hens in a row"></div>
  <h5 class="abs" style="left:325px;top:21px">TESTIMONIALS</h5>
  <p class="abs" style="left:275px;top:44px;width:240px;font-size:8px;line-height:17px;color:#7a7068;text-align:justify">We have pipping and peeping! Pipping is when the chicks start the process of breaking out of their shells. While they're still in the egg they will start peeping. We have pipping and peeping! Pipping is when the chicks start the process of breaking out of their shells. While they're still in<br>&nbsp; - DanaK</p>
  <h5 class="abs" style="left:560px;top:21px">INQUIRIES</h5>
  <div class="abs field" style="left:560px;top:41px">Name</div>
  <div class="abs field" style="left:560px;top:64px">Email Address</div>
  <div class="abs field" style="left:560px;top:87px">Phone No#</div>
  <div class="abs field" style="left:560px;top:110px">Zip Code</div>
  <div class="abs btn" style="left:658px;top:130px;width:89px;height:21px;line-height:21px">SUBMIT</div>
</section>

<footer class="abs footer">
  <h6 class="abs" style="left:117px;top:32px">SUBSCRIBE TO OUR NEWSLETTER</h6>
  <p class="abs" style="left:120px;top:52px;font-size:8.5px;color:var(--muted)">Sign up to get special events and updates</p>
  <div class="abs" style="left:117px;top:71px;width:187px;height:22px;background:#1a1918;border:1px solid #555;font-size:8px;color:#777;padding:6px 8px">Enter Email Address.*</div>
  <div class="abs" style="left:263px;top:72px;width:40px;height:20px;background:#3a3836;color:#999;font-size:9px;text-align:center;line-height:20px">›</div>
  <h6 class="abs" style="left:823px;top:32px">FOLLOW US ON</h6>
  <div class="abs sq" style="left:825px;top:54px;background:#3b5a9a"></div>
  <div class="abs sq" style="left:862px;top:54px;background:#3aa9dc"></div>
  <div class="abs sq" style="left:898px;top:54px;background:#e58a1f"></div>
  <p class="abs" style="right:90px;top:141px;font-size:8px;color:#ddd">Copyright © 2013 Lease-A-Goose. All Rights Reserved</p>
</footer>

<div class="abs fb">
  <div class="abs" style="left:3px;top:3px;width:36px;height:28px;border:1px solid #ccc;background:#f3efe6"></div>
  <p class="abs" style="left:45px;top:3px;font-size:9.5px;color:#3b5998;font-weight:700">Lease-A-Goose <span style="font-weight:400;font-size:8px">on Pagebook</span></p>
  <div class="abs" style="left:46px;top:17px;width:38px;height:14px;border:1px solid #ccc;background:#f4f4f4;font-size:7.5px;color:#888;padding:2px 6px">✓ Like</div>
  <p class="abs" style="left:95px;top:19px">You like this.</p>
  <div class="abs" style="left:0;top:36px;width:239px;height:1px;background:#ddd"></div>
  <p class="abs" style="left:4px;top:40px">5,009 people like <b>Lease-A-Goose</b>.</p>
  <div class="abs av" style="left:5px;top:52px"></div><div class="abs av" style="left:51px;top:52px"></div><div class="abs av" style="left:96px;top:52px"></div><div class="abs av" style="left:141px;top:52px"></div><div class="abs av" style="left:187px;top:52px"></div>
  <p class="abs" style="left:8px;top:87px;font-size:7px;word-spacing:24px">Meera Ravi Kishan Nisha Varun</p>
  <p class="abs" style="left:4px;top:98px;font-size:7px;color:#3b5998">▪ Pagebook social plugin</p>
</div>

<nav class="abs flinks"><span>Home</span><span>About Us</span><span>Products</span><span>Services</span><span>FAQ's</span><span>Contact Us</span><span>Partner Register</span></nav>

</body>
</html>
```